New year's card Meridian Vehicle Handlers

We would like to receive a digital Christmas/New Year's card for our company with focus on sustainability.
website: www.mvhdocklands.com

```html
<!DOCTYPE html>
<html lang="en">
<head>
<meta charset="utf-8">
<title>Meridian Vehicle Handlers – Happy New Year 2022</title>
<link rel="stylesheet" href="https://fonts.googleapis.com/css2?family=Permanent+Marker&family=Tinos:wght@400;700&family=Anton&display=swap">
<style>
  :root {
    --page: #f4f4f4;
    --navy-deep: #0a1640;
    --navy: #0f2766;
    --royal: #1a3f95;
    --sky: #33b5e8;
    --ice: #6fd6f7;
    --gold-light: #f3d6a8;
    --gold: #c9a877;
    --gold-dark: #8c7350;
    --ink: #14204a;
    --white: #ffffff;
  }
  * { margin: 0; padding: 0; box-sizing: border-box; }
  html, body {
    width: 1200px; height: 1000px; overflow: hidden;
    background: var(--page);
  }
  .canvas { position: relative; width: 1200px; height: 1000px; }
  .card {
    position: absolute; left: 78px; top: 110px;
    width: 1044px; height: 738px; overflow: hidden;
    background: var(--navy-deep);
  }
  .card-art, .card-type { position: absolute; inset: 0; width: 100%; height: 100%; }

  .brand {
    position: absolute; left: 52px; top: 78px;
    display: flex; align-items: center; gap: 12px;
  }
  .brand-dot {
    width: 22px; height: 22px; border-radius: 50%;
    background: var(--ice);
  }
  .brand-name {
    font-family: "Tinos", "Times New Roman", serif;
    font-weight: 700; font-size: 28px;
    color: var(--white); line-height: 1.1;
    width: 230px;
  }

  .greeting-happy {
    font-family: "Permanent Marker", cursive;
    font-size: 170px;
  }
  .greeting-newyear {
    font-family: "Tinos", "Times New Roman", serif;
    font-weight: 700; font-size: 165px;
    fill: var(--ice);
  }
  .year-digit {
    font-family: "Anton", "Arial Narrow", sans-serif;
    font-size: 190px;
  }

  .wheel {
    position: absolute; left: 417px; top: 482px;
    width: 136px; height: 136px; border-radius: 50%;
    background: radial-gradient(circle, var(--gold-light) 0%, var(--gold) 35%, var(--gold-dark) 60%, #1b1b1f 64%, #2a2a30 100%);
  }
  .photo-car {
    position: absolute;
    background: linear-gradient(180deg, #1c2c55 0%, #0c1530 70%, #070b18 100%);
    border-radius: 40px 60px 14px 14px;
  }
  .photo-car.left { left: 0; top: 497px; width: 288px; height: 200px; }
  .photo-car.right { left: 757px; top: 512px; width: 287px; height: 200px; }

  .website {
    position: absolute; left: 0; width: 100%; top: 676px;
    text-align: center;
    font-family: "Tinos", "Times New Roman", serif;
    font-size: 24px; color: var(--ink);
  }
</style>
</head>
<body>
<div class="canvas">
  <div class="card">
    <svg class="card-art" viewBox="78 110 1044 738" xmlns="http://www.w3.org/2000/svg" aria-hidden="true">
      <defs>
        <radialGradient id="bowl" cx="0.5" cy="0.55" r="0.6">
          <stop offset="0" stop-color="#1d48a6"/>
          <stop offset="1" stop-color="#0e2462"/>
        </radialGradient>
        <radialGradient id="glow" cx="0.5" cy="0.5" r="0.5">
          <stop offset="0" stop-color="#ffffff"/>
          <stop offset="0.25" stop-color="#d9f3ff" stop-opacity="0.9"/>
          <stop offset="1" stop-color="#6fd6f7" stop-opacity="0"/>
        </radialGradient>
        <radialGradient id="floor" cx="0.5" cy="0.5" r="0.5">
          <stop offset="0" stop-color="#6fd6f7" stop-opacity="0.9"/>
          <stop offset="0.5" stop-color="#2a8de0" stop-opacity="0.6"/>
          <stop offset="1" stop-color="#1a3f95" stop-opacity="0"/>
        </radialGradient>
      </defs>
      <rect x="78" y="110" width="1044" height="738" fill="#0a1640"/>
      <path d="M78 560 C90 380 260 250 560 190 C400 230 200 300 110 420 C90 460 80 520 78 560 Z" fill="#1e6db5"/>
      <ellipse cx="600" cy="560" rx="505" ry="345" fill="url(#bowl)"/>
      <path d="M600 110 L1122 110 L1122 848 L1010 848 C1100 700 1085 450 905 305 C810 225 710 160 600 110 Z" fill="#33b5e8"/>
      <path d="M470 116 C720 120 990 190 1122 300 L1122 250 C990 160 800 112 640 110 Z" fill="#6fd6f7"/>
      <path d="M78 790 C260 820 420 840 560 848 L78 848 Z" fill="#1e6db5"/>
      <ellipse cx="600" cy="765" rx="330" ry="38" fill="url(#floor)"/>
      <circle cx="820" cy="145" r="70" fill="url(#glow)"/>
      <circle cx="120" cy="410" r="48" fill="url(#glow)"/>
      <g fill="#6fd6f7" opacity="0.5">
        <circle cx="335" cy="600" r="2"/><circle cx="860" cy="640" r="2"/>
        <circle cx="700" cy="570" r="1.5"/><circle cx="450" cy="600" r="1.5"/>
        <circle cx="960" cy="380" r="2"/><circle cx="180" cy="520" r="1.5"/>
      </g>
    </svg>

    <div class="brand">
      <span class="brand-dot"></span>
      <span class="brand-name">Meridian Vehicle Handlers</span>
    </div>

    <div class="wheel" role="img" aria-label="Gold alloy car wheel standing in for the zero"></div>

    <svg class="card-type" viewBox="0 0 1044 738" xmlns="http://www.w3.org/2000/svg">
      <defs>
        <linearGradient id="gold" x1="0" y1="0" x2="0" y2="1">
          <stop offset="0" stop-color="#f3d6a8"/>
          <stop offset="0.55" stop-color="#c9a877"/>
          <stop offset="1" stop-color="#8c7350"/>
        </linearGradient>
      </defs>
      <text class="greeting-happy" x="262" y="318" textLength="500" lengthAdjust="spacingAndGlyphs" fill="url(#gold)">HAPPY</text>
      <text class="greeting-newyear" x="152" y="432" textLength="740" lengthAdjust="spacingAndGlyphs">New Year</text>
      <text class="year-digit" x="297" y="635" textLength="100" lengthAdjust="spacingAndGlyphs" fill="url(#gold)">2</text>
      <text class="year-digit" x="552" y="635" textLength="85" lengthAdjust="spacingAndGlyphs" fill="url(#gold)">2</text>
      <text class="year-digit" x="637" y="635" textLength="95" lengthAdjust="spacingAndGlyphs" fill="url(#gold)">2</text>
    </svg>

    <div class="photo-car left" role="img" aria-label="Photo of a dark blue sedan, front three-quarter view"></div>
    <div class="photo-car right" role="img" aria-label="Photo of a dark blue sedan, front three-quarter view"></div>

    <div class="website">www.mvhdocklands.com</div>
  </div>
</div>
</body>
</html>
```